Business Card Design Project

We need a business card design for a new boutique consulting company, TivaConsulting. Our new logo has just been designed and we are looking for simple, clean looking business cards. Logo attached

Industry/Entity Type

Boutique

Requirements
Must have
• There must be room for each card to have the following details:
Name
Title
Address - 2 lines
Phone number
Email address
Website address

Nice to have
• May have something on the back of the buisness card - emphasing the word "Tiva".

```html
<!DOCTYPE html>
<html lang="en">
<head>
<meta charset="utf-8">
<title>TivaConsulting Business Card</title>
<link rel="stylesheet" href="https://fonts.googleapis.com/css2?family=Source+Sans+3:wght@400&display=swap">
<style>
  :root {
    --board: #ffffff;
    --board-line: #3a3a3a;
    --charcoal: #58585a;
    --ink: #4d4d4f;
    --paper: #ffffff;
    --green-light: #9ccf4a;
    --green-dark: #5fa52e;
    --card-edge: #2b2b2b;
    --shadow: rgba(0, 0, 0, 0.35);
  }
  html, body {
    margin: 0;
    padding: 0;
    overflow: hidden;
    background: var(--board);
  }
  .board {
    position: relative;
    width: 1200px;
    height: 849px;
    box-sizing: border-box;
    border: 1.5px solid var(--board-line);
    background: var(--board);
    overflow: hidden;
  }
  .card {
    position: absolute;
    box-sizing: border-box;
    box-shadow: 6px 8px 8px var(--shadow);
  }
  .card-front {
    left: 51px;
    top: 301px;
    width: 472px;
    height: 287px;
    background: var(--charcoal);
  }
  .brand-band {
    position: absolute;
    left: 0;
    top: 107px;
    width: 100%;
    height: 85px;
    background: var(--paper);
    display: flex;
    align-items: center;
    justify-content: center;
  }
  .brand-name {
    font-family: "Source Sans 3", "Myriad Pro", sans-serif;
    font-weight: 400;
    font-size: 60px;
    line-height: 1;
    color: var(--charcoal);
  }
  .card-back {
    left: 678px;
    top: 304px;
    width: 470px;
    height: 290px;
    background: var(--paper);
    border: 1.5px solid var(--card-edge);
    overflow: hidden;
  }
  .contact {
    position: absolute;
    left: 44px;
    top: 101px;
    margin: 0;
    font-family: "Source Sans 3", "Myriad Pro", sans-serif;
    font-weight: 400;
    font-size: 15.5px;
    line-height: 20.6px;
    color: var(--ink);
    font-style: normal;
  }
  .contact span {
    display: block;
  }
  .green-band {
    position: absolute;
    left: 0;
    bottom: 0;
    width: 100%;
    height: 54px;
    background: linear-gradient(to bottom, var(--green-light), var(--green-dark));
  }
</style>
</head>
<body>
  <main class="board">
    <section class="card card-front" aria-label="Card front">
      <div class="brand-band">
        <span class="brand-name">TivaConsulting</span>
      </div>
    </section>

    <section class="card card-back" aria-label="Card back">
      <address class="contact">
        <span class="contact-name">Sam Placeholder</span>
        <span class="contact-street">42 Sample Street</span>
        <span class="contact-town">Sampleville 3000</span>
        <span class="contact-phone">09 55512 3401</span>
        <span class="contact-web">www.tivaconsulting.com</span>
        <span class="contact-email">sam@tivaconsulting.com</span>
      </address>
      <div class="green-band"></div>
    </section>
  </main>
</body>
</html>
```